App Store Screenshot Design for Vaccination Record App (iOS)

Project Description
We are looking for a professional graphic designer to redesign our App Store screenshots for our iOS app Medlo, a personal vaccination record app.
The goal is to significantly improve App Store conversion by creating screenshots that look:
• Clean
• Trustworthy
• Modern
• Medical but friendly
• Suitable for parents and older adults
Our current screenshots feel too “developer-like.” We want to match or exceed the visual quality of top competitors in this category.
⸻
About the App
Medlo helps people:
• Store all their vaccinations in one place
• Upload and scan vaccination proofs. Medlo automatically recognizes vaccines from photos, making imports fast and effortless.
• Receive reminders for boosters and expiring vaccinations
• Manage profiles for family members
• Export records (PDF) for school, work, or travel
Target users:
• Parents (tracking children’s vaccinations)
• Adults 45+
• Travelers
• Caregivers
This is not a children’s app — it’s a serious health utility that must feel reliable and credible.
⸻
Target Audience
Primary:
• Parents
• Older adults (45+)
Secondary:
• Travelers
• Caregivers
Design should feel:
• Calm
• Reassuring
• Clear
• Easy to understand at a glance
⸻
What We Need
1. App Store Screenshot Designs
• iPhone and iPad format (Apple App Store guidelines)
• Approx. 5–7 screenshots
• Focus on benefits, not features
• Short, strong headlines
• Clean UI framing
Important:
These screenshots are marketing visuals for the App Store.
They do NOT need to reflect the app UI 1:1.
You may crop, frame, abstract, or stylize the app screens to improve clarity and conversion.
2. Editable Figma File
This is very important.
All text in the screenshots must be:
• Easily editable in Figma
• Not baked into images
• Structured so we can localize into multiple languages (EN, NL, DE, FR, ES)
Think:
• Text layers
• Components
• Smart layout for longer translations
⸻
Style & Visual Direction
We like:
• Clean gradients
• Medlo orange / trustworthy colors
• Real people (optional but preferred)
• Subtle medical cues (e.g. bandage / plaster on arm)
We specifically like the first screenshot of this competitor:
👉 https://apps.quorvane.example/us/app/shotlog-tracker/id4827150396
(The woman with a bandage on her arm works very well.)
We want a similar level of polish, but not a copy.
We strongly encourage designers to explore two visual directions:
• A safe, refined direction closely aligned with the current app UI
• A more conceptual / aspirational direction focused on trust, peace of mind, and emotional reassurance
We are open to combining the best elements of both.
Color guidance:
Medlo’s brand color is orange.
Designs should feel medical and trustworthy, but must remain clearly aligned with our brand.
Avoid switching to generic blue-only medical palettes.
⸻
What We Don’t Want
• Overly playful or childish designs
• Overloaded screens
• Technical / developer-style visuals
• Stock images that feel fake or cheesy
⸻
Deliverables
• App Store screenshot designs (iphone and ipad)
• Fully editable Figma file
• Clear text hierarchy
• Ready for localization
⸻
Success Criteria
Primary goal:
Increase App Store page conversion (install rate).
A successful design:
• Looks immediately trustworthy
• Clearly communicates value in <3 seconds
• Feels competitive with top health apps
• Improves App Store conversion
⸻
References
Our app (current version):
https://apps.quorvane.example/us/app/medlo-vaccination-record/id7381029546
Competitor we admire visually:
https://apps.quorvane.example/us/app/shotlog-tracker/id4827150396
⸻
Extra Context (Optional for Designers)
This app already has:
• 200k users
• Active international expansion
• Paid subscriptions
This is not a hobby project — we are investing in quality.

```html
<!DOCTYPE html>
<html lang="en">
<head>
<meta charset="utf-8">
<title>App Store Screenshots – Vaccination Record</title>
<link href="https://fonts.googleapis.com/css2?family=Poppins:wght@400;500;600;700&family=Inter:wght@400;500;600;700&display=swap" rel="stylesheet">
<style>
:root{
  --canvas:#f4f5f7;
  --panel-top:#f3f7fd;
  --panel-bottom:#e4edfb;
  --ink:#15213a;
  --muted:#7d889c;
  --line:#e7ebf2;
  --orange:#f7a21b;
  --orange-soft:#fff1da;
  --blue:#2f6ff0;
  --blue-soft:#5a92f7;
  --green:#2fae6b;
  --red:#e9503f;
  --frame:#1c1d22;
  --white:#ffffff;
}
*{box-sizing:border-box;margin:0;padding:0}
html,body{width:893px;height:1200px;overflow:hidden;background:var(--canvas)}
body{font-family:"Inter",sans-serif;color:var(--ink)}
.gallery{
  position:absolute;left:36px;top:36px;
  display:grid;grid-template-columns:repeat(3,259px);grid-template-rows:repeat(2,548px);
  column-gap:23px;row-gap:30px;
}
.shot{
  position:relative;overflow:hidden;border-radius:4px;
  background:linear-gradient(180deg,var(--panel-top),var(--panel-bottom));
}
.shot-title{
  position:absolute;left:0;right:0;top:32px;text-align:center;
  font-family:"Poppins",sans-serif;font-weight:400;font-size:20px;line-height:1.3;color:var(--ink);
  padding:0 14px;
}
.shot-title strong{font-weight:700}
.wave{position:absolute;left:0;bottom:0;width:259px;height:170px}
.phone{
  position:absolute;left:36px;top:118px;width:188px;height:450px;
  background:var(--white);border:6px solid var(--frame);border-radius:30px;overflow:hidden;
  box-shadow:0 14px 30px rgba(25,45,90,.18);
}
.phone::before{content:"";position:absolute;top:6px;left:50%;width:54px;height:14px;margin-left:-27px;background:var(--frame);border-radius:10px}
.screen{padding:30px 11px 0;font-size:7px}
.screen-title{font-family:"Poppins",sans-serif;font-size:11px;font-weight:600;margin-bottom:8px}
.row{display:flex;align-items:center;gap:6px;padding:6px 0;border-bottom:1px solid var(--line)}
.row-name{font-weight:600;font-size:7.5px}
.row-sub{color:var(--muted);font-size:6px;margin-top:2px}
.tag{display:inline-block;margin-top:3px;padding:1px 5px;border-radius:6px;font-size:5.5px;font-weight:600;color:var(--white);background:var(--green)}
.tag.due{background:var(--red)}
.tag.soon{background:var(--orange)}
.thumb{width:30px;height:22px;border-radius:3px;background:linear-gradient(135deg,#e9e3d6,#c9c0ae);flex:none}
.avatar{width:20px;height:20px;border-radius:50%;background:linear-gradient(135deg,#d8c3ae,#a88d76);flex:none}
.tab-bar{position:absolute;left:0;right:0;bottom:0;height:38px;border-top:1px solid var(--line);background:var(--white);display:flex;justify-content:space-around;align-items:center}
.tab-bar i{width:10px;height:10px;border-radius:3px;background:#c5ccd8}
.fab{position:absolute;right:12px;bottom:48px;width:22px;height:22px;border-radius:50%;background:var(--orange);color:var(--white);font-size:15px;line-height:22px;text-align:center;font-weight:600}
.pill{position:absolute;background:var(--white);border-radius:10px;box-shadow:0 8px 20px rgba(25,45,90,.16);padding:8px 10px;font-size:8px}
.users-badge{
  position:absolute;left:50%;top:20px;width:128px;margin-left:-64px;padding:10px 8px 8px;
  background:var(--white);border-radius:14px;box-shadow:0 8px 20px rgba(25,45,90,.12);text-align:center;
}
.users-badge .mark{display:block;width:22px;height:22px;margin:0 auto 4px;border-radius:6px;background:var(--orange)}
.users-badge p{font-family:"Poppins",sans-serif;font-weight:700;font-size:16px;line-height:1.15}
.art{position:absolute;border-radius:50%}
.btn{display:block;margin:8px auto;width:90%;padding:5px 0;border-radius:8px;background:var(--orange);color:var(--white);text-align:center;font-weight:600;font-size:7px}
.flag{width:14px;height:10px;border-radius:2px;flex:none}
</style>
</head>
<body>
<main class="gallery">

  <section class="shot">
    <div class="users-badge"><span class="mark"></span><p>Over 10k+<br>users</p></div>
    <h2 class="shot-title" style="top:112px;font-size:19px">One Secure Place<br><strong>for Vaccines</strong></h2>
    <svg class="wave" viewBox="0 0 259 170" aria-hidden="true"><path d="M0 90 C80 40 170 150 259 70 V170 H0Z" fill="var(--blue-soft)" opacity=".55"/><path d="M0 120 C90 80 170 170 259 110 V170 H0Z" fill="var(--blue)"/></svg>
    <div class="phone" style="top:180px">
      <div class="screen">
        <p class="screen-title">My Vaccinations</p>
        <div class="row"><div><p class="row-name">Hepatitis A</p><p class="row-sub">Dose 2 of 2</p><span class="tag">Complete</span></div></div>
        <div class="row"><div><p class="row-name">Hepatitis B</p><p class="row-sub">Dose 3 of 3</p><span class="tag">Complete</span></div></div>
        <div class="row"><div><p class="row-name">Typhoid Fever</p><p class="row-sub">Booster due</p><span class="tag due">Due soon</span></div></div>
        <div class="row"><div><p class="row-name">Smallpox</p><p class="row-sub">Single dose</p><span class="tag soon">Reminder</span></div></div>
      </div>
      <div class="fab">+</div>
      <div class="tab-bar"><i></i><i></i><i></i><i></i></div>
    </div>
  </section>

  <section class="shot">
    <h2 class="shot-title">Upload &amp; Store<br><strong>Proofs Instantly</strong></h2>
    <svg class="wave" viewBox="0 0 259 170" aria-hidden="true"><path d="M0 90 C80 40 170 150 259 70 V170 H0Z" fill="var(--blue-soft)" opacity=".55"/><path d="M0 120 C90 80 170 170 259 110 V170 H0Z" fill="var(--blue)"/></svg>
    <div class="phone">
      <div class="screen">
        <p class="screen-title">Uploads</p>
        <div class="row"><div class="thumb" role="img" aria-label="Photo of a vaccination card"></div><div><p class="row-name">Vaccine card</p><p class="row-sub">Added 12 Mar</p></div></div>
        <div class="row"><div class="thumb" role="img" aria-label="Photo of a vaccination certificate"></div><div><p class="row-name">Travel record</p><p class="row-sub">Added 04 Feb</p></div></div>
        <div class="row"><div class="thumb" role="img" aria-label="Photo of a booster receipt"></div><div><p class="row-name">Booster proof</p><p class="row-sub">Added 21 Jan</p></div></div>
        <div class="row"><div class="thumb" role="img" aria-label="Photo of a clinic letter"></div><div><p class="row-name">Clinic letter</p><p class="row-sub">Added 09 Dec</p></div></div>
        <div class="row"><div class="thumb" role="img" aria-label="Photo of a school form"></div><div><p class="row-name">School form</p><p class="row-sub">Added 30 Nov</p></div></div>
      </div>
      <div class="fab">+</div>
      <div class="tab-bar"><i></i><i></i><i></i><i></i></div>
    </div>
    <div class="art" role="img" aria-label="Floating photo of a vaccination document" style="left:185px;top:96px;width:44px;height:36px;border-radius:6px;background:linear-gradient(135deg,#8ed0a0,#f6c46a)"></div>
  </section>

  <section class="shot">
    <h2 class="shot-title"><strong>Never Miss a<br>Booster Again</strong></h2>
    <svg class="wave" viewBox="0 0 259 170" aria-hidden="true"><path d="M0 90 C80 40 170 150 259 70 V170 H0Z" fill="var(--blue-soft)" opacity=".55"/><path d="M0 120 C90 80 170 170 259 110 V170 H0Z" fill="var(--blue)"/></svg>
    <div class="phone">
      <div class="screen">
        <p class="screen-title">My Vaccinations</p>
        <div class="row"><div><p class="row-name">Hepatitis A</p><p class="row-sub">Dose 2 of 2</p><span class="tag">Complete</span></div></div>
        <div class="row"><div><p class="row-name">Typhoid Fever</p><p class="row-sub">Booster due</p><span class="tag due">Due soon</span></div></div>
      </div>
      <div class="tab-bar"><i></i><i></i><i></i><i></i></div>
    </div>
    <div class="pill" style="left:22px;top:262px;width:170px"><p class="row-name" style="font-size:11px">Smallpox</p><p class="row-sub" style="font-size:7px">Booster in 3 days</p></div>
    <div class="art" role="img" aria-label="Golden reminder bell" style="left:186px;top:236px;width:46px;height:46px;background:radial-gradient(circle at 40% 35%,#ffd978,#f0a623)"></div>
  </section>

  <section class="shot">
    <h2 class="shot-title">Vaccines for the<br><strong>Whole Family</strong></h2>
    <svg class="wave" viewBox="0 0 259 170" aria-hidden="true"><path d="M0 90 C80 40 170 150 259 70 V170 H0Z" fill="var(--blue-soft)" opacity=".55"/><path d="M0 120 C90 80 170 170 259 110 V170 H0Z" fill="var(--blue)"/></svg>
    <div class="phone">
      <div class="screen">
        <p class="screen-title">Family</p>
        <div class="row"><div class="avatar" role="img" aria-label="Family member photo"></div><div><p class="row-name">Anna Weller</p><p class="row-sub">6 vaccines</p></div></div>
        <div class="row"><div class="avatar" role="img" aria-label="Family member photo"></div><div><p class="row-name">Lucas Weller</p><p class="row-sub">4 vaccines</p></div></div>
        <div class="row"><div class="avatar" role="img" aria-label="Family member photo"></div><div><p class="row-name">Mia Weller</p><p class="row-sub">5 vaccines</p></div></div>
        <div class="row"><div class="avatar" role="img" aria-label="Family member photo"></div><div><p class="row-name">Noah Weller</p><p class="row-sub">3 vaccines</p></div></div>
        <div class="row"><div class="avatar" role="img" aria-label="Family member photo"></div><div><p class="row-name">Eva Weller</p><p class="row-sub">2 vaccines</p></div></div>
      </div>
      <div class="fab">+</div>
      <div class="tab-bar"><i></i><i></i><i></i><i></i></div>
    </div>
    <div class="art" role="img" aria-label="Vaccine syringe" style="left:196px;top:96px;width:38px;height:38px;border-radius:8px;background:linear-gradient(135deg,#bcd4fb,#4f86f2)"></div>
  </section>

  <section class="shot">
    <h2 class="shot-title"><strong>Plan vaccinations</strong><br>With Confidence</h2>
    <svg class="wave" viewBox="0 0 259 170" aria-hidden="true"><path d="M0 90 C80 40 170 150 259 70 V170 H0Z" fill="var(--blue-soft)" opacity=".55"/><path d="M0 120 C90 80 170 170 259 110 V170 H0Z" fill="var(--blue)"/></svg>
    <div class="phone">
      <div class="screen">
        <p class="screen-title">Good morning</p>
        <div style="background:var(--orange-soft);border-radius:8px;padding:7px">
          <p class="row-sub" style="font-size:6.5px;color:var(--ink)">Discover which vaccinations you need for your next trip</p>
          <span class="btn">Start Trip Planner</span>
        </div>
        <p class="row-name" style="margin-top:10px">My Trips</p>
        <div class="row"><span class="flag" style="background:#f2b233"></span><p class="row-name">Sri Lanka</p><p class="row-sub" style="margin-left:auto">Jun 2025</p></div>
        <div class="row"><span class="flag" style="background:#d9384a"></span><p class="row-name">Thailand</p><p class="row-sub" style="margin-left:auto">Aug 2025</p></div>
        <div class="row"><span class="flag" style="background:#2e9e55"></span><p class="row-name">Brazil</p><p class="row-sub" style="margin-left:auto">Nov 2025</p></div>
      </div>
      <div class="tab-bar"><i></i><i></i><i></i><i></i></div>
    </div>
    <div class="art" role="img" aria-label="Airplane in flight" style="left:186px;top:240px;width:46px;height:30px;border-radius:14px;background:linear-gradient(135deg,#e6eefc,#9dbaf0)"></div>
  </section>

  <section class="shot">
    <h2 class="shot-title">Personalised Travel<br><strong>Vaccine Advice</strong></h2>
    <svg class="wave" viewBox="0 0 259 170" aria-hidden="true"><path d="M0 90 C80 40 170 150 259 70 V170 H0Z" fill="var(--blue-soft)" opacity=".55"/><path d="M0 120 C90 80 170 170 259 110 V170 H0Z" fill="var(--blue)"/></svg>
    <div class="phone">
      <div class="screen">
        <p class="screen-title">Plan My Travel Shots</p>
        <div class="row"><span class="flag" style="background:#3b66c4"></span><p class="row-name">France</p></div>
        <div class="row"><span class="flag" style="background:#2e9e55"></span><p class="row-name">Mexico</p></div>
        <div class="row"><span class="flag" style="background:#d9384a"></span><p class="row-name">Indonesia</p></div>
      </div>
      <div class="tab-bar"><i></i><i></i><i></i><i></i></div>
    </div>
    <div class="pill" style="left:14px;top:262px;width:232px">
      <div style="display:flex;align-items:center;gap:6px;margin-bottom:4px"><span class="flag" style="background:#d9384a"></span><p class="row-name" style="font-size:11px">Indonesia</p></div>
      <div class="row"><p class="row-name">Hepatitis A</p><span class="tag" style="margin-left:auto">Recommended</span></div>
      <div class="row"><p class="row-name">Typhoid</p><span class="tag" style="margin-left:auto">Recommended</span></div>
      <div class="row" style="border:0"><p class="row-name">Rabies</p><span class="tag soon" style="margin-left:auto">Consider</span></div>
    </div>
    <svg style="position:absolute;left:200px;top:98px" width="34" height="34" viewBox="0 0 34 34" aria-hidden="true"><rect width="34" height="34" rx="9" fill="var(--blue-soft)"/><path d="M17 9v16M9 17h16" stroke="#fff" stroke-width="4" stroke-linecap="round"/></svg>
  </section>

</main>
</body>
</html>
```